A4 brochure to supporters | 4 page

Hi There. We have a brochure we need producing. We have a basic idea of what we are after including a rough mockup. Most items have the created so is just about coming up with an amazing looking design.
Kestrel Ridge Media is based in Springwood, QLD and services people right across Australia with Christian content - radio, Bible devotionals and online content.

Target Market(s)

Financial Supporters of Kestrel

Industry/Entity Type

Non Profit

Font styles to use
Other font styles liked:
• Proxima Nova is our corporate font.

Requirements
Must have
• Follow the basic design in the pdf - let me know if there are any elements missing from the files below

```html
<!DOCTYPE html>
<html lang="en">
<head>
<meta charset="utf-8">
<title>Kestrel Ridge Media – Supporter Brochure</title>
<link rel="stylesheet" href="https://fonts.googleapis.com/css2?family=Montserrat:ital,wght@0,400;0,500;0,600;0,700;0,800;1,700;1,800&family=Oswald:wght@300;600&family=Great+Vibes&display=swap">
<style>
:root{
  --blue:#27b1e6;
  --blue-deep:#1672b8;
  --navy:#1d2b48;
  --ink:#2a2a2a;
  --text:#555a60;
  --grey-band:#5b5d61;
  --panel:#eef0f2;
  --orange:#f4a21c;
  --stage:#e4e5e8;
  --paper:#ffffff;
}
*{box-sizing:border-box;margin:0;padding:0}
html,body{width:900px;height:1200px;overflow:hidden}
body{background:var(--stage);font-family:"Montserrat",Arial,sans-serif;color:var(--text);position:relative}

.spread{position:absolute;left:50px;width:800px;height:566px;display:flex;background:var(--paper);box-shadow:0 6px 18px rgba(0,0,0,.12)}
.spread--outer{top:22px}
.spread--inner{top:612px}
.page{position:relative;width:400px;height:566px;overflow:hidden}
.page + .page{border-left:1px solid #e3e3e3}

p{font-size:7.4px;line-height:1.45;margin-bottom:5px}
.heading-quote{font-style:italic;font-weight:800;color:var(--blue);font-size:16px;line-height:1.2;margin-bottom:10px}
.section-title{color:var(--blue);font-weight:700;font-size:10.5px;margin:8px 0 4px}
.section-title--lead{font-size:9.5px}

/* Back page */
.back{padding:26px 24px 0}
.stats{display:flex;border:1px solid var(--blue);background:var(--panel);height:140px;margin-top:10px}
.stats__photo{width:128px;background:linear-gradient(160deg,#cfe3ee 0%,#e9d6c4 55%,#9fb8c8 100%)}
.stats__list{list-style:none;padding:12px 10px 0 14px;flex:1}
.stats__list li{display:flex;align-items:center;gap:6px;height:20px}
.stats__box{width:10px;height:10px;border:1px solid #9aa0a6;flex:none}
.stats__num{color:var(--orange);font-weight:800;font-size:10.5px;width:62px}
.stats__label{font-size:6px;color:var(--text)}
.stats__note{font-size:5.8px;padding-left:16px;margin-top:3px}
.signoff{position:absolute;left:24px;right:24px;bottom:28px;display:flex;justify-content:space-between;align-items:flex-end}
.brand{display:flex;align-items:center;gap:6px}
.brand__mark{width:14px;height:14px;background:var(--blue)}
.brand__name{font-weight:800;font-size:12px;color:var(--navy);text-transform:uppercase;line-height:1.05;letter-spacing:.3px}
.tagline{font-weight:800;font-size:12px;color:var(--ink);line-height:1.1;position:relative;padding-right:58px}
.script{font-family:"Great Vibes",cursive;font-weight:400;color:var(--navy)}
.tagline .script{position:absolute;right:0;bottom:-8px;font-size:24px;line-height:1}

/* Cover */
.cover__photo{position:absolute;left:14px;right:0;top:28px;height:340px;background:linear-gradient(100deg,#2ab6ea 0%,#59c4ea 35%,#d36e8a 62%,#f39a2c 82%,#f6c530 100%)}
.cover__kicker{position:absolute;left:34px;top:48px;color:#fff;font-weight:700;font-size:9px;line-height:1.15}
.cover__kicker .script{display:block;color:#fff;font-size:34px;margin-top:-2px;padding-left:14px}
.cover__title{position:absolute;left:34px;top:150px;color:var(--navy);font-family:"Oswald",Arial,sans-serif}
.cover__title .light{display:block;font-weight:300;font-size:32px;line-height:1}
.cover__title .bold{display:block;font-weight:600;font-size:34px;line-height:1.05;color:#fff}
.cover__sub{display:block;font-family:"Montserrat",Arial,sans-serif;font-weight:600;font-size:12px;color:var(--navy);line-height:1.2;margin-top:4px;width:170px}
.cover__sub .script{font-size:22px;display:block;padding-left:20px}
.cover__foot{position:absolute;left:24px;right:24px;bottom:36px;display:flex;gap:12px;align-items:flex-start}
.badge{width:92px;height:62px;border:2px solid var(--blue);border-radius:4px;display:flex;align-items:center;justify-content:center;gap:5px;flex:none}
.badge .brand__mark{width:10px;height:10px}
.badge .brand__name{font-size:9px}
.arrow{width:0;height:0;border-top:7px solid transparent;border-bottom:7px solid transparent;border-left:9px solid var(--blue);margin-top:22px;flex:none}
.mission h4{color:var(--blue);font-size:9px;font-weight:700;margin-bottom:2px}
.mission p{font-size:7.6px;color:var(--ink)}
.url-pill{display:inline-block;background:var(--grey-band);color:#fff;font-weight:700;font-size:8px;letter-spacing:1.2px;padding:3px 16px;border-radius:2px;margin-top:4px}

/* Inner pages */
.inner{padding:26px 24px 0}
.intro{width:250px}
.quote-list{list-style:none;width:236px}
.quote-list li{position:relative;padding-left:14px;font-size:7.2px;line-height:1.45;margin-bottom:7px}
.quote-list li::before{content:"\201C";position:absolute;left:0;top:-4px;color:var(--blue);font-weight:800;font-size:15px}
.pie{position:absolute;right:18px;top:200px}
.giving{position:absolute;left:20px;right:20px;bottom:18px}
.giving__top{display:flex;align-items:center;justify-content:space-between;margin-bottom:6px}
.giving__band{background:var(--grey-band);color:#fff;font-weight:700;font-size:10px;letter-spacing:1.4px;text-align:center;padding:4px 0;margin-bottom:6px}
.contacts{display:flex;justify-content:space-around;list-style:none}
.contacts li{display:flex;flex-direction:column;align-items:center;gap:2px;font-size:7px;font-weight:700;color:var(--ink)}
.icon{width:12px;height:12px}

.gospel{padding:26px 22px 0}
.gospel__title{color:var(--blue);font-weight:800;font-size:15px;line-height:1.15;width:260px;margin-bottom:10px}
.stamp{position:absolute;right:22px;top:24px;width:44px;height:44px;border:2px solid #d9342b;border-radius:50%;display:flex;align-items:center;justify-content:center;text-align:center;color:#d9342b;font-weight:800;font-size:5.6px;line-height:1.2;transform:rotate(-12deg)}
.row{display:flex;gap:10px;align-items:flex-start}
.row p{flex:1}
.row > div{flex:1}
.photo-room{width:130px;height:82px;flex:none !important;background:linear-gradient(120deg,#c9a66b,#f1d26a 50%,#7c8c96)}
.sub{color:var(--blue);font-weight:700;font-size:7.8px;margin:5px 0 3px}
.sub b{color:var(--ink)}
.phone{width:30px;height:56px;border:2px solid var(--ink);border-radius:5px;background:linear-gradient(#f8f8f8,#e2eef5);flex:none !important}
.video{width:90px;height:54px;flex:none !important;background:linear-gradient(120deg,#2b2b2b,#8a5a3a 60%,#e0b04a)}
.stations{background:var(--panel);margin:8px -22px 0;padding:8px 22px 6px}
.map-fill{width:96px;height:72px;flex:none !important;background:var(--orange);border-radius:6px;display:flex;align-items:center;justify-content:center}
.map-fill span{font-size:6px;font-weight:700;color:var(--ink);background:#fff;padding:2px 4px;border-radius:2px}
</style>
</head>
<body>

<section class="spread spread--outer">
  <article class="page back">
    <h2 class="heading-quote">“I lift up my eyes to the mountains –<br>My help comes from the Lord,”</h2>
    <h3 class="section-title">True Hope comes from God</h3>
    <p>Humanity's search for meaning, fulfilment and hope is nothing new. With every generation comes new ideas and new struggles. Today's media and technology bombard us with promises of happiness, yet so many still feel lost, anxious and alone in a noisy world.</p>
    <p>There's a song we play on our radio network that beautifully captures the truth that Jesus is, and always will be, the only one who gives us true and lasting hope. He meets us right where we are, and His comfort reaches us in every season.</p>
    <p>This is the truth every Australian needs to hear, and it sits at the very heart of our mission.</p>
    <h3 class="section-title">We help people look to Him, 24/7</h3>
    <p>Right from day one, Kestrel's desire has been to communicate God's truth to every Australian. Our founders must have seemed a little crazy, with so few resources, but they had faith and a firm conviction that God would make a way.</p>
    <h3 class="section-title section-title--lead">Today, Kestrel is estimated to reach around 1 million people per month!</h3>
    <p>With your help, we bring Biblical truth, hope and insight through music, conversation, testimony and teaching, 24 hours a day, reaching people where they are through broadcast, print and digital media.</p>
    <div class="stats">
      <div class="stats__photo" role="img" aria-label="Photo of a woman looking out over the sea at sunrise"></div>
      <div>
        <ul class="stats__list">
          <li><span class="stats__box"></span><span class="stats__num">606,000</span><span class="stats__label">FM/AM Radio Listeners per month</span></li>
          <li><span class="stats__box"></span><span class="stats__num">100,000+</span><span class="stats__label">Online Listeners per quarter</span></li>
          <li><span class="stats__box"></span><span class="stats__num">165,000+</span><span class="stats__label">Daily Devotional distribution</span></li>
          <li><span class="stats__box"></span><span class="stats__num">330,000+</span><span class="stats__label">Podcast downloads per quarter</span></li>
          <li><span class="stats__box"></span><span class="stats__num">11 million</span><span class="stats__label">Kestrel App opened by users</span></li>
        </ul>
        <p class="stats__note">Plus a huge knock-on impact as the people we help reach out to others.</p>
      </div>
    </div>
    <footer class="signoff">
      <div class="brand"><span class="brand__mark"></span><span class="brand__name">Kestrel Ridge<br>Media</span></div>
      <div class="tagline">Helping People<br>Look to God<span class="script">Daily</span></div>
    </footer>
  </article>

  <article class="page cover">
    <div class="cover__photo" role="img" aria-label="Photo of a woman in profile blended with a sunrise over the ocean"></div>
    <div class="cover__kicker">Helping People<br>Look to God<span class="script">Daily</span></div>
    <h1 class="cover__title">
      <span class="light">LIVES ARE</span>
      <span class="bold">CHANGING</span>
      <span class="cover__sub">As we help people look to God<span class="script">Daily</span></span>
    </h1>
    <div class="cover__foot">
      <div class="badge"><span class="brand__mark"></span><span class="brand__name">Kestrel</span></div>
      <span class="arrow"></span>
      <div class="mission">
        <h4>Our mission</h4>
        <p>To be a trusted, consistent and unifying voice in the Australian Community to challenge, encourage &amp; affirm people in the Christian Faith.</p>
        <span class="url-pill">www.kestrelridge.org.au</span>
      </div>
    </div>
  </article>
</section>

<section class="spread spread--inner">
  <article class="page inner">
    <h2 class="heading-quote">Where does my help come from?<br>The Maker of heaven and earth.”</h2>
    <h3 class="section-title">Your support will help TODAY and IN THE FUTURE</h3>
    <p class="intro">Kestrel is only possible because of faithful supporters like you. Every gift keeps our radio, app and devotionals reaching people who need to hear that God is near, whether they are driving to work, sitting in hospital or lying awake at night.</p>
    <p class="intro"><strong>Please prayerfully consider how you can give to the Kestrel Mid-Year Appeal.</strong> Donations are tax deductible.</p>
    <h3 class="section-title">Here's what your support will do</h3>
    <ul class="quote-list">
      <li>Keep our stations on air around the clock, so lonely and hurting people can hear words of hope at any hour of the day or night. Many listeners tell us a song or a short devotion came at exactly the right moment.</li>
      <li>Build new tools like the Kestrel App and Kestrel Kids, sharing the gospel with the next generation in the places they spend their time, and giving families simple ways to grow in faith together.</li>
      <li>Extend our network into regional towns, so more communities across Australia can tune in to Christian content close to home, with local prayer and encouragement they can trust.</li>
      <li>Support our prayer team as they answer calls and messages every week, praying with people through grief, illness and hard seasons, and pointing them to a local church.</li>
    </ul>
    <svg class="pie" width="120" height="120" viewBox="0 0 120 120" aria-label="Pie chart of income: donations 64%">
      <circle cx="60" cy="60" r="58" fill="var(--blue-deep)"/>
      <path d="M60 60 L60 2 A58 58 0 0 0 4.8 42 Z" fill="var(--orange)"/>
      <path d="M60 60 L4.8 42 A58 58 0 0 0 2.6 68 Z" fill="#8cc63f"/>
      <path d="M60 60 L2.6 68 A58 58 0 0 0 9.8 89 Z" fill="#e2522c"/>
      <text x="38" y="66" fill="#fff" font-family="Montserrat, sans-serif" font-size="8.5" font-weight="700">Donation 64%</text>
    </svg>
    <footer class="giving">
      <div class="giving__top">
        <div class="brand"><span class="brand__mark"></span><span class="brand__name">Kestrel</span></div>
      </div>
      <div class="giving__band">PLEASE GIVE BY 30 JUNE</div>
      <ul class="contacts">
        <li><svg class="icon" viewBox="0 0 12 12"><circle cx="6" cy="6" r="6" fill="var(--blue)"/><circle cx="6" cy="6" r="3.4" fill="none" stroke="#fff" stroke-width="1"/><path d="M2.6 6h6.8M6 2.6v6.8" stroke="#fff" stroke-width=".8"/></svg>kestrelridge.org.au</li>
        <li><svg class="icon" viewBox="0 0 12 12"><circle cx="6" cy="6" r="6" fill="var(--blue)"/><path d="M4 3.2l1.2 1.6-.7.8c.5 1 1.1 1.6 2 2l.8-.7 1.6 1.2-.8 1.1C5.6 9 3 6.4 2.9 4z" fill="#fff"/></svg>1800 555 014</li>
        <li><svg class="icon" viewBox="0 0 12 12"><circle cx="6" cy="6" r="6" fill="var(--blue)"/><rect x="4" y="2.6" width="4" height="6.8" rx=".8" fill="#fff"/></svg>Kestrel app</li>
      </ul>
    </footer>
  </article>

  <article class="page gospel">
    <h2 class="gospel__title">We're passionate about communicating the gospel</h2>
    <div class="stamp">PROGRESS<br>UPDATE</div>
    <div class="row">
      <div>
        <p>Establishing the Kestrel Ridge Media Hub was our next big step in sharing God's Word with the nation. Thanks to your generosity, this new space now supports our radio, digital and devotional teams as they work together.</p>
        <p>The Hub is only one part of the plan. Here are some of the other key projects your gifts are making possible, helping people look to God today and into the future.</p>
      </div>
      <div class="photo-room" role="img" aria-label="Photo of the new media hub interior"></div>
    </div>
    <h4 class="sub">New Generation Kestrel App – <b>Just launched!</b></h4>
    <div class="row">
      <p>80% of Australians now own a smartphone, and our new app puts radio, devotionals, podcasts and prayer in one place. It's simple to use, free to download and already helping thousands of people meet with God wherever they are. Share it with a friend who needs hope today.</p>
      <div class="phone" role="img" aria-label="Phone showing the Kestrel App"></div>
    </div>
    <div class="row" style="margin-top:4px">
      <div class="video" role="img" aria-label="Video still of children from Kestrel Kids"></div>
      <div>
        <h4 class="sub">Kestrel Kids – Biblical truth for 8–12 year olds – <b>Just launched!</b></h4>
        <p>Short videos, stories and songs help children discover Jesus for themselves, with free resources for parents, churches and schools across the country.</p>
      </div>
    </div>
    <div class="stations">
      <div class="row">
        <div>
          <h4 class="sub">100+ New Stations by 2025 – <b>Eight so far!</b></h4>
          <p>On top of our network of 700+ stations, we are working hard to bring Christian radio to towns that have never had it. Eight new stations are now on air, with many more planned for the coming year.</p>
          <p>Please pray about how much you can give to Kestrel's Mid-Year Appeal.</p>
        </div>
        <div class="map-fill" role="img" aria-label="Map of Australia marking new station locations"><span>100+ New stations</span></div>
      </div>
    </div>
    <footer class="giving">
      <div class="giving__top">
        <div class="brand"><span class="brand__mark"></span><span class="brand__name">Kestrel</span></div>
      </div>
      <div class="giving__band">PLEASE GIVE BY 30 JUNE</div>
      <ul class="contacts">
        <li><svg class="icon" viewBox="0 0 12 12"><circle cx="6" cy="6" r="6" fill="var(--blue)"/><circle cx="6" cy="6" r="3.4" fill="none" stroke="#fff" stroke-width="1"/><path d="M2.6 6h6.8M6 2.6v6.8" stroke="#fff" stroke-width=".8"/></svg>kestrelridge.org.au</li>
        <li><svg class="icon" viewBox="0 0 12 12"><circle cx="6" cy="6" r="6" fill="var(--blue)"/><path d="M4 3.2l1.2 1.6-.7.8c.5 1 1.1 1.6 2 2l.8-.7 1.6 1.2-.8 1.1C5.6 9 3 6.4 2.9 4z" fill="#fff"/></svg>1800 555 014</li>
        <li><svg class="icon" viewBox="0 0 12 12"><circle cx="6" cy="6" r="6" fill="var(--blue)"/><rect x="4" y="2.6" width="4" height="6.8" rx=".8" fill="#fff"/></svg>Kestrel app</li>
      </ul>
    </footer>
  </article>
</section>

</body>
</html>
```